Lifecoach needs website design based on a standard Wordpress theme

I need a website for my new lifecoaching business that can be easily implemented in Wordpress, it needs to be compatible with a standard Wordpress theme. So I can place the pictures, texts etc. in a standard theme of Wordpress.

I want the design to be a very good feeling and playfull one, based on my logo.

Target Market(s)

I will coach people to reach their goals and dreams in life.

Industry/Entity Type

Business

Requirements
Must have
• Can be easy implemented in Wordpress.
Nice to have
• Photo's of nature are nice.

```html
<!DOCTYPE html>
<html lang="en">
<head>
<meta charset="utf-8">
<title>Ruben van Dijk Lifecoach</title>
<link href="https://fonts.googleapis.com/css2?family=Cinzel:wght@400;700&family=Open+Sans:ital,wght@0,400;0,600;0,700;1,400&display=swap" rel="stylesheet">
<style>
:root{
  --blue:#1b9fd8;
  --blue-light:#27bdef;
  --navy:#1d4f8c;
  --heading:#2a6cb0;
  --green:#5e9a2a;
  --text:#6a6a6a;
  --text-dark:#333;
  --band:#f0f0f0;
  --footer:#0e3560;
}
*{margin:0;padding:0;box-sizing:border-box}
html,body{width:1024px;height:1200px;overflow:hidden}
body{position:relative;background:#fbfdfd;font-family:'Open Sans',sans-serif;color:var(--text)}
.abs{position:absolute}
h1,h2{font-weight:400}

.site-header{left:0;top:0;width:1024px;height:96px;background:linear-gradient(#ececec,#f2f2f2);border-top:3px solid var(--navy)}
.brand-mark{left:138px;top:14px;width:72px;height:72px;border-radius:50%;border:4px solid var(--blue)}
.brand-name{left:218px;top:28px;font-family:'Cinzel',serif;font-size:25px;color:var(--navy);line-height:1;white-space:nowrap}
.brand-sub{left:270px;top:57px;font-family:'Cinzel',serif;font-size:15px;color:var(--navy);letter-spacing:1px}
.call{left:487px;top:37px;display:flex;align-items:center;gap:5px;font-size:13px;color:#8a8a8a;font-weight:600;white-space:nowrap}
.call b{color:var(--navy);font-weight:700}
.call-icon{width:19px;height:19px;background:var(--navy);border-radius:3px;display:flex;align-items:center;justify-content:center}
.cta{left:712px;top:26px;width:176px;height:40px;background:linear-gradient(var(--blue-light),#12a5e2);color:#fff;font-family:'Cinzel',serif;font-weight:700;font-size:12px;display:flex;align-items:center;justify-content:center;box-shadow:0 2px 4px rgba(0,0,0,.2);white-space:nowrap}

.main-nav{left:0;top:96px;width:1024px;height:41px;background:linear-gradient(#2ac3f3,#0e9fdb);border-bottom:1px solid #0a7fb5}
.main-nav a{position:absolute;top:11px;font-family:'Cinzel',serif;font-size:15px;color:#fff;text-decoration:none;letter-spacing:.5px;white-space:nowrap}

.hero{left:0;top:137px;width:1024px;height:421px;background:linear-gradient(180deg,#c9c3c0 0%,#a9b8a6 30%,#7fa03c 55%,#8aa22f 80%,#7a7a2a 100%)}
.hero-caption{left:0;top:262px;width:512px;height:184px;background:rgba(34,158,204,.85);padding:20px 0 0 135px;color:#fff}
.hero-caption h1{font-family:'Cinzel',serif;font-size:29px;line-height:35px;font-weight:700}
.hero-caption p{margin-top:14px;font-size:12.5px;font-weight:600;line-height:19px;width:330px}
.arrow{top:330px;width:48px;height:47px;background:rgba(30,40,40,.55);display:flex;align-items:center;justify-content:center}

.col-title{top:610px;width:240px;text-align:center;font-family:'Cinzel',serif;font-size:20px;color:var(--heading);letter-spacing:.3px;white-space:nowrap;line-height:26px}
.rule{top:650px;width:240px;height:3px;border-top:1px dotted #bbb;border-bottom:1px dotted #bbb}
.col-text{top:668px;width:240px;font-size:12.3px;line-height:19.5px}
.list{top:741px;list-style:none;font-size:13px}
.list li{height:25.6px;display:flex;align-items:center;gap:9px;white-space:nowrap}
.list li::before{content:"";border-left:5px solid #666;border-top:4px solid transparent;border-bottom:4px solid transparent}

.news-title{font-family:'Cinzel',serif;font-size:11px;color:var(--green);text-decoration:underline;font-weight:700;white-space:nowrap}
.news-thumb{width:68px;height:57px;border-radius:2px}
.news-body{font-size:9.5px;line-height:14.5px;width:160px}
.news-date{font-size:7.5px;font-weight:700;margin-top:4px}

.section-title{top:888px;width:1024px;text-align:center;font-family:'Cinzel',serif;font-size:21px;color:var(--heading);letter-spacing:.5px}
.card{top:934px;width:368px;height:120px;background:#f3f3f3;box-shadow:0 1px 3px rgba(0,0,0,.25)}
.avatar{left:38px;top:25px;width:70px;height:70px;border-radius:50%}
.quote{left:131px;top:30px;width:215px;font-style:italic;font-size:10.5px;line-height:16px}
.cite{left:131px;top:88px;font-size:10.5px;color:var(--text-dark)}
.cite b{font-weight:700}
.cite span{color:#aaa;margin:0 6px}

.newsletter{left:0;top:1090px;width:1024px;height:71px;background:var(--band);border-top:1px solid #e2e2e2}
.nl-title{left:129px;top:1108px;font-family:'Cinzel',serif;font-size:12.5px;color:var(--green);font-weight:700;white-space:nowrap}
.nl-sub{left:129px;top:1127px;font-size:9.5px}
.nl-input{left:346px;top:1110px;width:277px;height:31px;background:#fff;border:1px solid #d6d6d6;font-size:10px;padding:0 13px;line-height:29px;color:#888}
.nl-submit{left:623px;top:1110px;width:88px;height:31px;background:linear-gradient(var(--blue-light),#12a5e2);color:#fff;font-size:12px;font-weight:700;text-align:center;line-height:31px}
.social{top:1112px;width:27px;height:27px;border-radius:3px;box-shadow:0 1px 2px rgba(0,0,0,.3)}

.site-footer{left:0;top:1161px;width:1024px;height:39px;background:linear-gradient(#0b2d52,#164b80)}
.copy{left:128px;top:1173px;font-size:9.5px;color:#a8b8c8}
.foot-links{right:129px;top:1173px;font-size:9.5px;color:#8fb6dd}
.foot-links span{margin:0 8px;color:#6a8fb5}
</style>
</head>
<body>

<header class="site-header abs"></header>
<div class="brand-mark abs"></div>
<div class="brand-name abs">Ruben van Dijk</div>
<div class="brand-sub abs">Lifecoach</div>
<div class="call abs">
  <span class="call-icon"><svg width="12" height="12" viewBox="0 0 24 24"><path fill="#fff" d="M6.6 10.8a15.2 15.2 0 0 0 6.6 6.6l2.2-2.2a1 1 0 0 1 1-.25 11.4 11.4 0 0 0 3.6.57 1 1 0 0 1 1 1V20a1 1 0 0 1-1 1A17 17 0 0 1 3 4a1 1 0 0 1 1-1h3.5a1 1 0 0 1 1 1c0 1.25.2 2.45.57 3.57a1 1 0 0 1-.25 1z"/></svg></span>
  Call us today <b>+1800.555.0199</b>
</div>
<div class="cta abs">Schedule Appointment</div>

<nav class="main-nav abs">
  <a style="left:139px">Home</a>
  <a style="left:245px">About Me</a>
  <a style="left:384px">Rates and Services</a>
  <a style="left:594px">Common Questions</a>
  <a style="left:815px">Contact</a>
</nav>

<div class="hero abs" role="img" aria-label="Photo of green rolling hills with a winding road and farmhouses under a cloudy sky"></div>
<div class="hero-caption abs">
  <h1>Live the life you've imagined.</h1>
  <p>Lorem ipsum dolor sit amet, consectetur adipisicing elit, sed do eiusmod tempor incididunt ut labore et dolore magna aliqua. Ut enim ad minim</p>
</div>
<div class="arrow abs" style="left:0"><svg width="12" height="18"><path d="M10 2 3 9l7 7" stroke="#fff" stroke-width="2.2" fill="none"/></svg></div>
<div class="arrow abs" style="left:980px"><svg width="12" height="18"><path d="m2 2 7 7-7 7" stroke="#fff" stroke-width="2.2" fill="none"/></svg></div>

<h2 class="col-title abs" style="left:134px">Services</h2>
<div class="rule abs" style="left:138px"></div>
<p class="col-text abs" style="left:138px">Lorem ipsum dolor sit amet, consectetur adipisicing elit, sed do eiusmod tempor incididunt ut labore et dolore.</p>
<ul class="list abs" style="left:138px">
  <li>Counselling</li><li>General Counselling</li><li>Trauma Therapy</li><li>Consultation</li>
</ul>

<h2 class="col-title abs" style="left:393px">Consultation Hours</h2>
<div class="rule abs" style="left:393px"></div>
<p class="col-text abs" style="left:393px">Lorem ipsum dolor sit amet, consectetur adipisicing elit, sed do eiusmod tempor incididunt ut labore et dolore.</p>
<ul class="list abs" style="left:393px">
  <li style="font-weight:600">Monday - Friday</li><li style="font-weight:600">9:00 am - 6:00pm</li><li>Call us at: +1800.555.0199</li><li>Email: info@brightpathcoach.com</li>
</ul>

<h2 class="col-title abs" style="left:650px">Latest News</h2>
<div class="rule abs" style="left:648px"></div>
<div class="news-title abs" style="left:650px;top:672px">Trauma Therapy Can Help</div>
<div class="news-thumb abs" style="left:647px;top:694px;background:linear-gradient(#cfd2d4,#8e8f92)" role="img" aria-label="Photo of a person in a hooded jacket by the sea"></div>
<div class="abs" style="left:729px;top:691px">
  <p class="news-body">The point of using Lorem Ipsum is that it has a more-or-less normal distribution of letters, as opposed..</p>
  <p class="news-date">▫ 8 December 2013</p>
</div>
<div class="news-title abs" style="left:650px;top:773px">5 Tips for better outlook in life</div>
<div class="news-thumb abs" style="left:647px;top:794px;background:linear-gradient(#b9d2c9,#6e8f6c)" role="img" aria-label="Photo of a misty lake with a wooden pier"></div>
<div class="abs" style="left:729px;top:792px">
  <p class="news-body">The point of using Lorem Ipsum is that it has a more-or-less normal distribution of letters, as opposed..</p>
  <p class="news-date">▫ 8 December 2013</p>
</div>

<h2 class="section-title abs">Client Testimonials</h2>
<div class="card abs" style="left:133px">
  <div class="avatar abs" style="background:linear-gradient(#8a7565,#5e4c42)" role="img" aria-label="Portrait photo of a smiling male client"></div>
  <p class="quote abs">“Lorem ipsum dolor sit amet, consectetur adipisicing elit, sed do eiusmod tempor incididunt ut labore et dolore magna aliqua.</p>
  <p class="cite abs"><b>Daniel Moss</b><span>|</span>Oakline Co.</p>
</div>
<div class="card abs" style="left:518px">
  <div class="avatar abs" style="background:linear-gradient(#7a5a48,#3e2c24)" role="img" aria-label="Portrait photo of a smiling female client"></div>
  <p class="quote abs">“Lorem ipsum dolor sit amet, consectetur adipisicing elit, sed do eiusmod tempor incididunt ut labore et dolore magna aliqua.</p>
  <p class="cite abs"><b>Daniel Moss</b><span>|</span>Oakline Co.</p>
</div>

<section class="newsletter abs"></section>
<div class="nl-title abs">Subscribe to our Newsletter</div>
<div class="nl-sub abs">Get the latest updates about mental health</div>
<div class="nl-input abs">Enter Your Email Address</div>
<div class="nl-submit abs">Submit</div>
<div class="social abs" style="left:761px;background:#3b5c9a" aria-label="Social link"></div>
<div class="social abs" style="left:798px;background:#3aa0d8" aria-label="Social link"></div>
<div class="social abs" style="left:834px;background:#1a73ac" aria-label="Social link"></div>
<div class="social abs" style="left:869px;background:#d63a2b" aria-label="Social link"></div>

<footer class="site-footer abs"></footer>
<div class="copy abs">Copyright © 2014 BrightPath Coaching. All Rights Reserved.</div>
<div class="foot-links abs">Site Map<span>•</span>Privacy Policy<span>•</span>Contact Us</div>

</body>
</html>
```